Business Card cabinets and cabinets components making company.

the card should be formal and interesting at the same time. The main colors will be black and white.

Font styles to use
Sans Serif

Colors

Designer to choose only greyscale colors for use in the design.

Requirements
Must have
• At least must have the followings:
office phone
cell phone
address
position
name
email
web

```html
<!DOCTYPE html>
<html lang="en">
<head>
<meta charset="utf-8">
<title>TrimFit Business Card</title>
<link rel="stylesheet" href="https://fonts.googleapis.com/css2?family=Montserrat:wght@400;500;600;700&display=swap">
<style>
  :root {
    --bg: #1c1c1c;
    --ink: #111111;
    --card-black: #141414;
    --paper: #ffffff;
    --grey: #9a9a9a;
    --grey-text: #6e6e6e;
  }
  * { box-sizing: border-box; margin: 0; padding: 0; }
  html, body {
    width: 1200px; height: 900px; overflow: hidden;
    background: var(--bg);
    font-family: "Montserrat", sans-serif;
  }
  .canvas { position: relative; width: 1200px; height: 900px; }
  .card {
    position: absolute; left: 280px; width: 640px; height: 366px;
    overflow: hidden; box-shadow: 0 14px 30px rgba(0,0,0,.55);
  }
  .card--front { top: 50px; background: var(--card-black); }
  .card--back { top: 484px; background: var(--card-black); }

  .front-swoosh { position: absolute; inset: 0; }

  .identity { position: absolute; right: 56px; top: 26px; text-align: right; }
  .identity__name { font-size: 28px; font-weight: 600; letter-spacing: 1px; color: var(--ink); }
  .identity__position { font-size: 14px; font-weight: 500; color: var(--ink); margin-top: 2px; }
  .identity__rule { height: 2px; width: 230px; background: var(--grey); margin: 6px 0 0 auto; }

  .contacts { position: absolute; right: 20px; top: 112px; list-style: none; }
  .contacts__item {
    display: flex; align-items: flex-start; justify-content: flex-end;
    gap: 12px; margin-bottom: 9px;
  }
  .contacts__text { font-size: 11.5px; line-height: 1.35; color: var(--grey-text); text-align: right; }
  .contacts__icon {
    width: 22px; height: 22px; border-radius: 5px; background: var(--ink);
    flex: none; display: flex; align-items: center; justify-content: center;
  }

  .brand {
    position: absolute; font-weight: 700; letter-spacing: -1px;
    display: flex; align-items: center; gap: 12px;
  }
  .brand__square { width: 28px; height: 28px; border: 4px solid currentColor; }
  .brand--front { left: 96px; top: 226px; font-size: 58px; color: var(--ink); }
  .brand--back { left: 0; right: 0; top: 112px; justify-content: center; font-size: 70px; color: var(--paper); }

  .back-band {
    position: absolute; left: 0; right: 0; bottom: 0; height: 66px;
    background: var(--grey);
    display: flex; align-items: center; justify-content: center;
  }
  .back-band__web { font-size: 17px; font-weight: 500; color: #333333; letter-spacing: .5px; }
</style>
</head>
<body>
<main class="canvas">

  <section class="card card--front" aria-label="Card front">
    <svg class="front-swoosh" viewBox="0 0 640 366" width="640" height="366" aria-hidden="true">
      <rect width="640" height="366" fill="var(--card-black)"/>
      <path d="M60,0 C10,70 0,150 0,190 L0,215 C8,140 30,60 78,0 Z" fill="var(--grey)"/>
      <path d="M96,0 C14,130 14,354 200,356 C430,358 600,330 640,292 L640,0 Z" fill="var(--grey)"/>
      <path d="M110,0 C30,130 30,342 200,342 C420,344 590,318 640,280 L640,0 Z" fill="var(--paper)"/>
      <path d="M122,0 C72,60 50,130 50,205" fill="none" stroke="var(--card-black)" stroke-width="12"/>
    </svg>

    <header class="identity">
      <h1 class="identity__name">YOUR NAME</h1>
      <p class="identity__position">Profession/Position</p>
      <div class="identity__rule"></div>
    </header>

    <ul class="contacts">
      <li class="contacts__item">
        <span class="contacts__text">000-1234-5678<br>000-1234-5678</span>
        <span class="contacts__icon">
          <svg width="13" height="13" viewBox="0 0 24 24" aria-hidden="true"><path fill="#fff" d="M6.6 10.8a15 15 0 0 0 6.6 6.6l2.2-2.2a1 1 0 0 1 1-.25 11.4 11.4 0 0 0 3.6.57 1 1 0 0 1 1 1V20a1 1 0 0 1-1 1A17 17 0 0 1 3 4a1 1 0 0 1 1-1h3.5a1 1 0 0 1 1 1c0 1.25.2 2.45.57 3.57a1 1 0 0 1-.25 1z"/></svg>
        </span>
      </li>
      <li class="contacts__item">
        <span class="contacts__text">name@trimfitcabinets.com</span>
        <span class="contacts__icon">
          <svg width="13" height="13" viewBox="0 0 24 24" aria-hidden="true"><path fill="#fff" d="M3 5h18v14H3z M4 6l8 6 8-6" stroke="#111" stroke-width="1.5"/></svg>
        </span>
      </li>
      <li class="contacts__item">
        <span class="contacts__text">www.trimfitcabinets.com</span>
        <span class="contacts__icon">
          <svg width="13" height="13" viewBox="0 0 24 24" aria-hidden="true"><circle cx="12" cy="12" r="9" fill="none" stroke="#fff" stroke-width="2"/><path d="M3 12h18M12 3c3 3 3 15 0 18M12 3c-3 3-3 15 0 18" fill="none" stroke="#fff" stroke-width="1.5"/></svg>
        </span>
      </li>
      <li class="contacts__item">
        <span class="contacts__text">4821 Maple Ridge Lane<br>Riverton, VA 24500</span>
        <span class="contacts__icon">
          <svg width="13" height="13" viewBox="0 0 24 24" aria-hidden="true"><path fill="#fff" d="M12 2a7 7 0 0 0-7 7c0 5 7 13 7 13s7-8 7-13a7 7 0 0 0-7-7zm0 9.5A2.5 2.5 0 1 1 12 6.5a2.5 2.5 0 0 1 0 5z"/></svg>
        </span>
      </li>
    </ul>

    <div class="brand brand--front">
      <span class="brand__square"></span>
      <span class="brand__name">TrimFit</span>
    </div>
  </section>

  <section class="card card--back" aria-label="Card back">
    <div class="brand brand--back">
      <span class="brand__square"></span>
      <span class="brand__name">TrimFit</span>
    </div>
    <footer class="back-band">
      <span class="back-band__web">www.trimfitcabinets.com</span>
    </footer>
  </section>

</main>
</body>
</html>
```